App Design - Job Poise Lantern

We require an App Design for our new App called 'Poise Lantern'. This app is essentially an assistant to help Users prepare for job interviews, to help them get hired. <br/><br/>Users who download the App can view common Questions and Answers, save their favourite responses and also view common Interview Tips. <br/><br/>The vision for our App is for Users who are preparing for an interview (1 week before, 1 day before, even 1 hour before), are able to download, view and educate themselves on common questions and responses, and then be confident to land the job. <br/><br/>Our team has developed wireframes to help highlight what each screen should do and include. Please see attached document, which also highlights key requirements for the experience. Feel free to add/remove/edit what you see on these wireframes. Our preference is that you use Adobe XD please.<br/><br/>In terms of design guidelines, we want the experience to be simple, intuitive and 'memorable' to help Users to remember the questions/responses when they are in the interview. <br/><br/>The final design should communicate 'neat and clean professionalism'; we like the design of: vocatia hub com au<br/><br/>Thank you for reading! Good luck !

Target Market(s)

Professional job seekers

Font styles to use
Sans Serif

Colors

Designer to choose colors to be used in the design.

Requirements
Must have
• Please see my PixelBazaar_UX file that I have uploaded
Nice to have
• Could you also please include some ideas on how we can incorporate Advertising into the app screens

```html
<!DOCTYPE html>
<html lang="en">
<head>
<meta charset="utf-8">
<title>Poise Lantern – App Screens</title>
<link href="https://fonts.googleapis.com/css2?family=Nunito+Sans:wght@400;600;700;800&display=swap" rel="stylesheet">
<style>
:root{
  --canvas:#f1f1f2;
  --screen:#f3f4f8;
  --card:#ffffff;
  --card-active:#e1e4ea;
  --ink:#4a4a4a;
  --ink-soft:#6a6a6a;
  --line:#8a8a8a;
  --teal:#10d2c6;
  --blue:#4f63fb;
}
*{box-sizing:border-box;margin:0;padding:0}
html,body{width:1200px;height:1199px;overflow:hidden;background:var(--canvas)}
body{font-family:"Nunito Sans",sans-serif;color:var(--ink)}
.board{position:absolute;left:0;top:0;width:1932px;height:1930px;transform:scale(.6211);transform-origin:0 0}
.screen{position:absolute;width:309px;height:545px;background:var(--screen);overflow:hidden;box-shadow:0 2px 6px rgba(0,0,0,.08)}
.abs{position:absolute}
.topbar{position:absolute;left:0;top:16px;width:100%;height:24px;font-size:15px;font-weight:700}
.topbar .back{position:absolute;left:18px;top:0;font-weight:400;display:flex;align-items:center;gap:6px}
.topbar .app{position:absolute;left:97px;top:1px}
.topbar .app.center{left:0;width:100%;text-align:center}
.title{position:absolute;left:0;width:100%;text-align:center;font-size:23px;font-weight:700}
.sub{position:absolute;left:20px;right:20px;text-align:center;font-size:13px;line-height:16px;color:var(--ink-soft)}
.card{position:absolute;left:16px;width:277px;background:var(--card);border-radius:10px;box-shadow:0 3px 8px rgba(0,0,0,.06);padding:14px 12px 0 23px;font-size:12.5px;line-height:16.3px;color:var(--ink-soft)}
.card.active{background:var(--card-active)}
.card b{display:block;font-weight:700;color:var(--ink);font-size:13.5px;margin-bottom:1px}
.card p{padding-left:12px}
.card.para p{padding-left:0}
.panel{position:absolute;left:16px;width:277px;background:var(--card);border-radius:10px;box-shadow:0 3px 8px rgba(0,0,0,.06)}
.opt{position:absolute;left:32px;width:245px;height:44px;border:1px solid var(--line);border-radius:10px;font-size:15px;display:flex;align-items:center;justify-content:center;background:#fff}
.opt.on{background:var(--teal);border-color:var(--teal);color:#fff;font-weight:600}
.cta{position:absolute;left:69px;width:171px;height:51px;border-radius:26px;background:var(--blue);color:#fff;font-size:15px;font-weight:700;display:flex;align-items:center;justify-content:center;box-shadow:0 4px 8px rgba(79,99,251,.3)}
.nav{position:absolute;width:10px;height:14px}
.nav.l{left:3px}.nav.r{right:6px}
.more{position:absolute;left:146px;width:16px;height:20px}
</style>
</head>
<body>
<div class="board">

  <!-- Welcome -->
  <section class="screen" style="left:230px;top:110px">
    <h1 class="title" style="top:60px;font-size:30px;font-weight:800">Poise Lantern</h1>
    <p class="sub" style="top:116px;font-size:15px;line-height:20px">Your guide to most common interview questions, and the best responses to help you get hired</p>
    <svg class="abs" style="left:80px;top:217px" width="150" height="150" viewBox="0 0 150 150">
      <circle cx="75" cy="75" r="66" fill="#fff" stroke="var(--teal)" stroke-width="12"/>
      <text x="75" y="86" text-anchor="middle" font-family="Nunito Sans, sans-serif" font-size="30" fill="var(--ink)">Ready</text>
    </svg>
    <div class="cta" style="top:441px">Get Started</div>
  </section>

  <!-- Menu -->
  <section class="screen" style="left:613px;top:110px">
    <div class="topbar"><span class="app center">Poise Lantern</span></div>
    <div class="panel" style="top:56px;height:358px"></div>
    <h2 class="title" style="top:108px;line-height:30px">Choose according to<br>current needs!</h2>
    <div class="opt" style="top:213px">View Questions &amp; Responses</div>
    <div class="opt on" style="top:276px">My Question Portfolio</div>
    <div class="opt" style="top:338px">Interview Tips</div>
    <div class="cta" style="top:440px">Continue</div>
  </section>

  <!-- Categories -->
  <section class="screen" style="left:1008px;top:108px">
    <div class="topbar"><span class="back"><svg width="8" height="13"><path d="M7 1L2 6.5 7 12" fill="none" stroke="#555" stroke-width="2"/></svg>Back</span><span class="app">Poise Lantern</span></div>
    <div class="panel" style="top:56px;height:358px"></div>
    <h2 class="title" style="top:66px;line-height:30px">View Questions &amp;<br>Responses</h2>
    <p class="sub" style="top:144px">Select your question category</p>
    <div class="opt" style="top:172px">Technical</div>
    <div class="opt" style="top:229px">Behavioural</div>
    <div class="opt on" style="top:285px">Situational</div>
    <div class="opt" style="top:342px">Motivational</div>
    <svg class="more" style="top:421px" viewBox="0 0 16 20"><path d="M2 3l6 6 6-6M2 11l6 6 6-6" fill="none" stroke="#888" stroke-width="1.6"/></svg>
    <div class="cta" style="top:453px">Next</div>
  </section>

  <!-- Behavioural list -->
  <section class="screen" style="left:1400px;top:112px">
    <div class="topbar"><span class="back"><svg width="8" height="13"><path d="M7 1L2 6.5 7 12" fill="none" stroke="#555" stroke-width="2"/></svg>Back</span><span class="app">Poise Lantern</span></div>
    <h2 class="title" style="top:60px">Behavioural</h2>
    <div class="card" style="top:98px;height:114px"><b>1. Implement idea</b><p>Give me an example of a new idea or initiative you have suggested to your manager. How did you implement this idea?</p></div>
    <div class="card" style="top:231px;height:114px"><b>2. What did you learn?</b><p>Give me an example of a time when you made a mistake or didn't deliver on expectations, what happened? What did you learn?</p></div>
    <div class="card" style="top:363px;height:84px"><b>3. Frustrate you</b><p>What parts of your current role frustrate you?</p></div>
    <div class="card" style="top:467px;height:90px"><b>4. Describe in three words</b><p>How would your colleagues describe you in three words?</p></div>
  </section>

  <!-- Response 1 -->
  <section class="screen" style="left:228px;top:725px">
    <div class="topbar"><span class="back"><svg width="8" height="13"><path d="M7 1L2 6.5 7 12" fill="none" stroke="#555" stroke-width="2"/></svg>Back</span><span class="app">Poise Lantern</span></div>
    <h2 class="title" style="top:60px">Response</h2>
    <div class="card active" style="top:98px;height:114px"><b style="font-weight:600">1. Implement idea</b><p>Give me an example of a new idea or initiative you have suggested to your manager. How did you implement this idea?</p></div>
    <svg class="nav r" style="top:148px" viewBox="0 0 10 14"><path d="M2 1l6 6-6 6" fill="none" stroke="#999" stroke-width="1.5"/></svg>
    <div class="card" style="top:230px;height:114px"><b style="font-weight:600">Response 1</b><p>I was attracted to this organisation because of the culture and what I have read on Staffsay Reviews. I was very impressed.</p></div>
    <div class="card" style="top:363px;height:114px"><b style="font-weight:600">Response 2</b><p>I was attracted to this organisation because of the culture and what I have read on Staffsay Reviews. I was very impressed.</p></div>
    <div class="card" style="top:495px;height:114px"><b style="font-weight:600">Response 3</b><p>I was attracted to this organisation</p></div>
  </section>

  <!-- Response 2 -->
  <section class="screen" style="left:618px;top:729px">
    <div class="topbar"><span class="back"><svg width="8" height="13"><path d="M7 1L2 6.5 7 12" fill="none" stroke="#555" stroke-width="2"/></svg>Back</span><span class="app">Poise Lantern</span></div>
    <h2 class="title" style="top:60px">Response</h2>
    <div class="card active" style="top:98px;height:114px"><b style="font-weight:600">2. What did you learn?</b><p>Give me an example of a time when you made a mistake or didn't deliver on expectations, what happened? What did you learn?</p></div>
    <svg class="nav l" style="top:148px" viewBox="0 0 10 14"><path d="M8 1L2 7l6 6" fill="none" stroke="#999" stroke-width="1.5"/></svg>
    <svg class="nav r" style="top:148px" viewBox="0 0 10 14"><path d="M2 1l6 6-6 6" fill="none" stroke="#999" stroke-width="1.5"/></svg>
    <div class="card" style="top:230px;height:114px"><b style="font-weight:600">Response 1</b><p>I was attracted to this organisation because of the culture and what I have read on Staffsay Reviews. I was very impressed.</p></div>
    <div class="card" style="top:363px;height:114px"><b style="font-weight:600">Response 2</b><p>I was attracted to this organisation because of the culture and what I have read on Staffsay Reviews. I was very impressed.</p></div>
    <div class="card" style="top:495px;height:114px"><b style="font-weight:600">Response 3</b><p>I was attracted to this organisation</p></div>
  </section>

  <!-- Portfolio -->
  <section class="screen" style="left:1009px;top:731px">
    <div class="topbar"><span class="back"><svg width="8" height="13"><path d="M7 1L2 6.5 7 12" fill="none" stroke="#555" stroke-width="2"/></svg>Back</span><span class="app">Poise Lantern</span></div>
    <h2 class="title" style="top:60px">My Question Portfolio</h2>
    <p class="sub" style="top:98px">These are you saved answer that you favourited we placed them here to help you</p>
    <div class="card" style="top:148px;height:114px"><b>4. What are your greatest strengths?</b><p>I was attracted to this organisation because of the culture and what I have read on Staffsay Reviews. I was very impressed.</p></div>
    <div class="card" style="top:280px;height:114px"><b>20. Where do you see your self in five</b><p>I was attracted to this organisation because of the culture and what I have read on Staffsay Reviews. I was very impressed.</p></div>
    <div class="card" style="top:412px;height:114px"><b>36. Why should we hire you?</b><p>I was attracted to this organisation because of the culture and what I have read on Staffsay Reviews. I was very impressed.</p></div>
  </section>

  <!-- Tips categories -->
  <section class="screen" style="left:1400px;top:732px">
    <div class="topbar"><span class="back"><svg width="8" height="13"><path d="M7 1L2 6.5 7 12" fill="none" stroke="#555" stroke-width="2"/></svg>Back</span><span class="app">Poise Lantern</span></div>
    <div class="panel" style="top:56px;height:274px"></div>
    <h2 class="title" style="top:66px">Interview Tips</h2>
    <p class="sub" style="top:107px">Select your interview tip category</p>
    <div class="opt" style="top:134px">Tips for before the interview</div>
    <div class="opt" style="top:190px">Tips for during the interview</div>
    <div class="opt on" style="top:247px">Tips for after the interview</div>
    <svg class="more" style="top:344px" viewBox="0 0 16 20"><path d="M2 3l6 6 6-6M2 11l6 6 6-6" fill="none" stroke="#888" stroke-width="1.6"/></svg>
    <div class="cta" style="top:453px">Next</div>
  </section>

  <!-- Tip detail 7 -->
  <section class="screen" style="left:229px;top:1335px">
    <div class="topbar"><span class="back"><svg width="8" height="13"><path d="M7 1L2 6.5 7 12" fill="none" stroke="#555" stroke-width="2"/></svg>Back</span><span class="app">Poise Lantern</span></div>
    <h2 class="title" style="top:60px">Response</h2>
    <div class="card active" style="top:98px;height:76px"><b style="font-weight:600">7. Prepared</b><p>Be prepared with examples of your work</p></div>
    <svg class="nav l" style="top:130px" viewBox="0 0 10 14"><path d="M8 1L2 7l6 6" fill="none" stroke="#999" stroke-width="1.5"/></svg>
    <svg class="nav r" style="top:130px" viewBox="0 0 10 14"><path d="M2 1l6 6-6 6" fill="none" stroke="#999" stroke-width="1.5"/></svg>
    <div class="card para" style="top:200px;height:178px;padding-top:24px"><p>During the interview, you will likely be asked about specific work you've completed in relation to the position. After reviewing the job description, think of work you've done in post jobs, clubs or volunteer positions that show you have experience and success doing the work they require.</p></div>
  </section>

  <!-- Tip detail 5 -->
  <section class="screen" style="left:619px;top:1338px">
    <div class="topbar"><span class="back"><svg width="8" height="13"><path d="M7 1L2 6.5 7 12" fill="none" stroke="#555" stroke-width="2"/></svg>Back</span><span class="app">Poise Lantern</span></div>
    <h2 class="title" style="top:60px">Response</h2>
    <div class="card active" style="top:98px;height:76px"><b style="font-weight:600">5. Recruit</b><p>Recruit a friend to practice answering</p></div>
    <svg class="nav l" style="top:130px" viewBox="0 0 10 14"><path d="M8 1L2 7l6 6" fill="none" stroke="#999" stroke-width="1.5"/></svg>
    <svg class="nav r" style="top:130px" viewBox="0 0 10 14"><path d="M2 1l6 6-6 6" fill="none" stroke="#999" stroke-width="1.5"/></svg>
    <div class="card para" style="top:200px;height:178px;padding-top:24px"><p>During the interview, you will likely be asked about specific work you've completed in relation to the position. After reviewing the job description, think of work you've done in post jobs, clubs or volunteer positions that show you have experience and success doing the work they require.</p></div>
  </section>

  <!-- Tips list -->
  <section class="screen" style="left:1010px;top:1339px">
    <div class="topbar"><span class="back"><svg width="8" height="13"><path d="M7 1L2 6.5 7 12" fill="none" stroke="#555" stroke-width="2"/></svg>Back</span><span class="app">Poise Lantern</span></div>
    <h2 class="title" style="top:60px">Interview Tips</h2>
    <div class="card" style="top:108px;height:85px"><b>1. Researching</b><p>Start by researching the company and your interviewrs</p></div>
    <div class="card" style="top:218px;height:85px"><b>2. Practice</b><p>Practice your answer to common interview questions</p></div>
    <div class="card" style="top:327px;height:85px"><b>3. Re-read</b><p>Re-read the job description</p></div>
    <div class="card" style="top:437px;height:85px"><b>4. Start Method</b><p>Use the start method in answering questions</p></div>
  </section>

</div>
</body>
</html>
```